We need a new brochure design for our dental clinic, Birchfield Dental. We have attached the information we want printed and photos to include.

Industry/Entity Type

Dental

```html
<!DOCTYPE html>
<html lang="en">
<head>
<meta charset="utf-8">
<title>Birchfield Dental Brochure</title>
<link href="https://fonts.googleapis.com/css2?family=Arimo:wght@400;700&family=Great+Vibes&family=Libre+Baskerville&display=swap" rel="stylesheet">
<style>
:root{
  --page:#e4e4e4;
  --ink:#231f20;
  --gold:#8c7a4f;
  --gold-light:#a8946a;
  --white:#ffffff;
  --red:#d6262b;
  --blue:#5fb3e0;
  --grey-text:#222;
}
*{box-sizing:border-box;margin:0;padding:0}
html,body{width:1200px;height:1000px;overflow:hidden;background:var(--page);font-family:"Arimo",Arial,sans-serif}
.brochure{position:absolute;left:200px;width:800px;box-shadow:6px 10px 18px rgba(0,0,0,.35)}

/* ---------- Outside spread ---------- */
.outside{top:14px;height:470px;background:var(--ink);display:flex;color:var(--white)}
.outside .panel{position:relative;height:100%}
.panel-bio{width:208px;border-right:1px dashed rgba(255,255,255,.5)}
.panel-contact{width:204px;border-right:1px dashed rgba(255,255,255,.5)}
.panel-cover{width:388px}
.photo{display:block}
.photo-doctor{height:200px;background:linear-gradient(160deg,#e8e6e2 0%,#cfcac4 45%,#3a3a44 100%)}
.photo-reception{height:200px;background:linear-gradient(180deg,#8a8176 0%,#b7ad9f 45%,#e6dfd2 100%)}
.gold-band{height:36px;background:var(--gold);padding:6px 14px}
.doctor-name{font-size:11px;font-weight:700;color:#f3ecd8}
.doctor-cred{font-size:6.5px;color:#f3ecd8;margin-top:2px}
.bio{padding:14px 14px 0;font-size:6.4px;line-height:1.45;color:#e8e8e8}
.bio p{margin-bottom:8px}

.brand{display:flex;align-items:center;gap:7px}
.brand-mark{width:30px;height:30px;border-radius:50%;background:var(--blue);flex:none}
.brand-name{font-size:20px;font-weight:400;color:var(--white);line-height:1}
.tagline{font-size:7.6px;letter-spacing:.3px;color:#ddd;margin-top:6px}

.contact-block{text-align:center;padding:18px 10px 0}
.contact-block .brand{justify-content:center}
.contact-block .brand-name{font-size:17px}
.address{font-size:6.4px;line-height:1.5;font-weight:700;margin-top:22px}
.hours{font-size:6.4px;line-height:1.5;font-weight:700;margin-top:12px}
.web{font-size:8px;font-weight:700;margin-top:14px}

.cover-head{padding:26px 0 0 22px}
.cover-head .brand-mark{width:40px;height:40px}
.cover-head .brand-name{font-size:24px}
.headline{padding-left:24px;margin-top:22px}
.headline .script{font-family:"Great Vibes",cursive;font-size:42px;line-height:1;color:var(--white)}
.headline .about{font-size:15px;color:var(--red);margin-left:108px;margin-top:-4px}
.headline .smile{font-size:52px;line-height:1;color:var(--white);margin-top:2px}
.photo-model{position:absolute;right:30px;bottom:0;width:215px;height:250px;border-radius:110px 110px 0 0;background:radial-gradient(ellipse at 50% 38%,#e9c3a8 0%,#c48d6c 38%,#4a2c20 75%,#231f20 100%)}

/* ---------- Inside spread ---------- */
.inside{top:500px;height:484px;background:var(--white);display:flex}
.col-left{width:262px;padding:10px 12px}
.col-right{width:538px;display:flex;flex-direction:column}
.photo-pain{height:128px;background:linear-gradient(135deg,#f4f4f4 0%,#d9d4cf 50%,#f09a52 100%)}
.body-text{font-size:6.6px;line-height:1.45;color:var(--grey-text);margin:8px 0}
.photo-xray{height:200px;background:radial-gradient(ellipse at 55% 50%,#e8771a 0%,#7a3a10 35%,#141414 70%,#0a0a0a 100%)}

.gold-section{background:var(--gold);height:192px;display:flex;gap:8px;padding:8px}
.tooth-col{width:128px}
.photo-tooth{height:82px;background:linear-gradient(160deg,#a79c8a 0%,#6e5f4b 50%,#c8bba7 100%)}
.gold-section .caption{font-size:6.3px;line-height:1.45;color:var(--white);margin-top:6px}
.smile-col{flex:1}
.photo-teeth{height:82px;background:linear-gradient(180deg,#f7f5f3 0%,#e9b7b2 40%,#ffffff 55%,#f2f0ee 100%)}
.philosophy{background:var(--ink);color:var(--white);font-family:"Libre Baskerville",Georgia,serif;font-size:8.4px;line-height:1.6;text-align:center;padding:6px 10px;text-transform:uppercase}
.tech-heading{font-family:"Libre Baskerville",Georgia,serif;font-size:8.4px;line-height:1.5;color:var(--gold);text-transform:uppercase;padding:8px 10px 6px}
.tech-area{display:flex;gap:10px;padding:0 10px}
.features{flex:1;display:flex;flex-direction:column;gap:8px}
.feature{display:flex;gap:8px;align-items:center}
.feature-photo{width:98px;height:50px;flex:none}
.feature-photo.lounge{background:linear-gradient(135deg,#cfe0e6,#7fa0a8)}
.feature-photo.chair{background:linear-gradient(135deg,#e9e2dc,#c9432f)}
.feature-photo.room{background:linear-gradient(135deg,#c9a8e8,#8e5cc4)}
.feature-text{font-size:6.4px;line-height:1.45;color:var(--grey-text)}
.services-col{width:158px}
.services{border:1px solid var(--gold);padding:3px}
.services-inner{border:1px solid var(--gold);padding:6px 4px;text-align:center;font-size:6.6px;line-height:1.5;color:var(--grey-text)}
.gold-box{background:var(--gold);color:var(--white);text-align:center;font-size:6.6px;padding:5px 4px;margin-top:6px}
.gold-box .phone{font-size:10px;font-weight:700;display:block;margin-top:2px}
</style>
</head>
<body>

<!-- Outside spread -->
<section class="brochure outside">
  <div class="panel panel-bio">
    <div class="photo photo-doctor" role="img" aria-label="Portrait of the dentist in dark scrubs in the clinic"></div>
    <div class="gold-band">
      <div class="doctor-name">Dr. Arjun K. Mehran</div>
      <div class="doctor-cred">B.D.S (S'pore), FPCDS (Pacific)</div>
    </div>
    <div class="bio">
      <p>Dr. Arjun K. Mehran obtained his BDS from Harbourview University. Upon graduation he served in various government institutions such as The Central Dental Institute, Public Wellness Board, National Defence Corps and Citycare Polyclinics.</p>
      <p>In 2009 Dr Arjun left the government sector for private practice. As a firm believer of continual education he is an alumni member of the Westlake Institute of Advanced Dental Studies. At the institute he received training from renowned dentists Dr Paul Hadley and Dr Lena Corrigan in the subjects of aesthetic restorative dentistry and root canal treatment.</p>
      <p>In 2014 Dr Arjun was admitted as a fellow at the prestigious Pacific College of Dental Surgeons. Dr Arjun has also completed his part 1 exams for the Diploma of Membership of the Joint Dental Faculties at the Northern College of Surgeons (MDF NCS).</p>
    </div>
  </div>

  <div class="panel panel-contact">
    <div class="photo photo-reception" role="img" aria-label="Clinic reception desk with flowers and receptionist"></div>
    <div class="gold-band"></div>
    <div class="contact-block">
      <div class="brand"><span class="brand-mark"></span><span class="brand-name">Birchfield Dental</span></div>
      <div class="tagline">A Healthier Smile For A Healthier You</div>
      <div class="address">
        212 Marlow Crescent Road<br>
        (Opposite Marlow Square and beside Juniper Bakery)<br>
        Singapore 418203<br>
        E-mail: info@birchfielddental.com.sg<br>
        Phone Number: +65 61204478
      </div>
      <div class="hours">
        Opening Hours:<br>
        Mondays - 11am - 8pm | Tuesdays - 9am - 6pm<br>
        Wednesdays 9am-6pm | Thursdays 11am-8pm<br>
        Fridays 9am-1pm | Saturdays 9am - 4pm<br>
        Sundays &amp; PH - closed
      </div>
      <div class="web">www.birchfielddental.com.sg</div>
    </div>
  </div>

  <div class="panel panel-cover">
    <div class="cover-head">
      <div class="brand"><span class="brand-mark"></span><span class="brand-name">Birchfield Dental</span></div>
      <div class="tagline">A Healthier Smile For A Healthier You</div>
    </div>
    <div class="headline">
      <div class="script">Feel great</div>
      <div class="about">about your</div>
      <div class="smile">Smile</div>
    </div>
    <div class="photo-model" role="img" aria-label="Smiling young woman resting her chin on her hand"></div>
  </div>
</section>

<!-- Inside spread -->
<section class="brochure inside">
  <div class="col-left">
    <div class="photo-pain" role="img" aria-label="Woman holding her head surrounded by words about facial pain, jaw lock and neck ache"></div>
    <p class="body-text">0% of dental diseases have little or no symptoms till advanced stages. When dental diseases reach an advanced stage the pain can be very sudden, intense and often accompanied by facial swelling. At this stage complex dental treatment would be needed to treat the tooth.</p>
    <div class="photo-xray" role="img" aria-label="Side profile x-ray illustration of a head highlighting the jaw joint"></div>
    <p class="body-text">Dental problems need not only be related to the teeth and gums. The health of the mouth depends on the harmonious inter-relationship between the teeth, muscles of the jaw and the temporomandibular joint. When an unhealthy relationship exists between these structures an individual can experience excessive tooth wear, shaky loose teeth, cracks or fractures, ear congestion, headaches, facial pain and postural problems.</p>
  </div>

  <div class="col-right">
    <div class="gold-section">
      <div class="tooth-col">
        <div class="photo-tooth" role="img" aria-label="Close-up of a cracked tooth with an old metal filling"></div>
        <p class="caption">The photo on the left shows a tooth with a mercury filling which has, over time, caused cracks to form along the tooth. These cracks are usually painless until they reach the nerve of the tooth. At this time the cracks can split the tooth and the pain can be sudden and excruciating.</p>
      </div>
      <div class="smile-col">
        <div class="photo-teeth" role="img" aria-label="Close-up of a bright white smile"></div>
        <p class="caption">Your smile may be saying more about you than you realise. Studies have shown that an attractive smile gives the perception of an individual to be successful, healthy and sociable. The same studies show that an unattractive smile gives the perception of an individual to be less successful, having a dull social life and even being less trustworthy. Of course these are just perceptions and often can be changed after getting to know a person in due time. However there may be instances where one does not get the benefit of time to make a lasting impression. Studies indicate that lasting impressions are made within the first three seconds of seeing someone. Cosmetic dentistry can greatly improve the attractiveness of a smile and help create a great first impression!</p>
      </div>
    </div>

    <div class="philosophy">At Birchfield Dental we believe in comprehensive dentistry.<br>It is our practice philosophy to focus on creating beautiful smiles<br>built on a healthy foundation. We call this functional aesthetics.</div>

    <div class="tech-heading">At Birchfield Dental, we believe in investing in state of the art technology<br>to ensure a comfortable dental experience for you.</div>

    <div class="tech-area">
      <div class="features">
        <div class="feature">
          <div class="feature-photo lounge" role="img" aria-label="Waiting lounge with refreshments"></div>
          <p class="feature-text">Feel free to relax and ask our friendly staff for some light refreshments before or after your dental treatment</p>
        </div>
        <div class="feature">
          <div class="feature-photo chair" role="img" aria-label="Modern red dental treatment chair"></div>
          <p class="feature-text">Our Aurora Treatment Centre provides excellent comfort for our patients with its advanced thermo upholstery and lumbar support.</p>
        </div>
        <div class="feature">
          <div class="feature-photo room" role="img" aria-label="Clinic corridor lit in soft purple light"></div>
          <p class="feature-text">A unique, comfortable and modern dental experience awaits you.</p>
        </div>
      </div>
      <div class="services-col">
        <div class="services">
          <div class="services-inner">
            Services Provided:<br>
            Dental Implants<br>
            Clear Aligners<br>
            Smile makeovers<br>
            Dental Orthopaedic Treatment<br>
            Braces for Children &amp; Adults<br>
            Dental fillings &amp; Porcelain restorations<br>
            Gum Treatments<br>
            Root canal Treatments<br>
            Wisdom tooth surgery<br>
            Dentures<br>
            Children's dentistry<br>
            Digital X-rays
          </div>
        </div>
        <div class="gold-box">0% interest free instalment plans available.</div>
        <div class="gold-box">Call us for an appointment today<span class="phone">+65 61204478</span></div>
      </div>
    </div>
  </div>
</section>

</body>
</html>
```